Web Design Project - Order A Moving Box for President Halvern (the product (box) has been designed

Create a web site design for a politically oriented project with an e-commerce function.

The webite will most likely only need to be 4 or 5 pages at the most; with one of those being an order page.

Please email with any questions.

Designers,

We have uploaded a excel file containing content and ideas.
We don;t have the product art back yet but you can leave a space on the "THe Box" page and the "Home" page.
Please email is you have any questions.

Thanks,
Dorin

Extension was added t allow more participation and updates from designers.

Target Market(s)

Conservation Voters, People who believe in the US Constitution, Capitalist, Entrepreneurs, Business Owners, Those who want to repeal HalvernCare

Industry/Entity Type

E-Commerce

Requirements
Must have
• Home Page
A Purpose and Mission Page (We have the content)
An order page

We have an outline of information that needs to be included.
You can email us directly at dorin@driftpack-away.com and we can forward the sketches and type for the site.
Nice to have
• 1. Links to a few (2 or 3)video clips if possible (will provide)
2. Links to voter registration website (will provide link)
3. Links to 4 or 5 other websites.

```html
<!DOCTYPE html>
<html lang="en">
<head>
<meta charset="utf-8">
<title>Move Out Box – Home</title>
<link rel="stylesheet" href="https://fonts.googleapis.com/css2?family=Cinzel:wght@400;700&family=Cabin+Condensed:wght@400&family=Roboto+Condensed:wght@400&family=Arimo:wght@400;700&display=swap">
<style>
  :root {
    --nav-bg-top: #2c2c2c;
    --nav-bg-bottom: #0d0d0d;
    --accent: #8fa63a;
    --accent-dark: #6f8526;
    --hero-bg: #353535;
    --hero-bg-dark: #222;
    --white: #ffffff;
    --text-soft: #e6e6e6;
    --panel: #eeeeee;
    --panel-edge: #cfcfcf;
    --footer-bg: #1a1a1a;
    --footer-bottom: #353535;
    --muted: #9a9a9a;
    --art-sky: #6a6af0;
    --art-grass: #a9d86a;
  }
  * { box-sizing: border-box; margin: 0; padding: 0; }
  html, body { width: 858px; height: 1200px; overflow: hidden; }
  body { position: relative; background: var(--footer-bg); font-family: "Arimo", Arial, sans-serif; color: var(--white); }

  .site-nav { position: absolute; left: 0; top: 0; width: 858px; height: 72px;
    background: linear-gradient(var(--nav-bg-top), var(--nav-bg-bottom));
    border-bottom: 3px solid var(--accent); }
  .site-nav ul { list-style: none; position: absolute; right: 8px; top: 31px; display: flex; gap: 22px; }
  .site-nav a { font-family: "Cinzel", serif; font-size: 18px; color: var(--white); text-decoration: none; letter-spacing: .5px; padding: 2px 6px; }
  .site-nav .is-current { background: var(--accent); border-radius: 5px; }

  .hero { position: absolute; left: 0; top: 75px; width: 858px; height: 693px;
    background: linear-gradient(180deg, var(--hero-bg) 0%, var(--hero-bg-dark) 100%); }
  .hero-rule { position: absolute; left: 0; top: 255px; width: 858px; height: 1px; background: #bbb; }
  .hero-headline { position: absolute; left: 0; top: 46px; width: 420px; text-align: center;
    font-family: "Cinzel", serif; font-weight: 700; font-size: 36px; line-height: 51px; letter-spacing: 1px; }
  .hero-subhead { position: absolute; left: 20px; top: 265px; width: 380px; text-align: center;
    font-family: "Cinzel", serif; font-size: 17px; line-height: 22px; }
  .hero-copy { position: absolute; left: 50px; top: 322px; width: 330px;
    font-family: "Roboto Condensed", sans-serif; font-size: 8.6px; line-height: 20px; color: var(--text-soft); }
  .hero-copy p { text-indent: 16px; }
  .hero-copy .big { font-size: 11px; }
  .hero-art { position: absolute; left: 412px; top: 25px; width: 426px; height: 290px; border: 2px solid #000;
    background: linear-gradient(180deg, var(--art-sky) 0%, var(--art-sky) 55%, var(--art-grass) 56%, var(--art-grass) 100%); }

  .box-claims { position: absolute; left: 475px; top: 326px; list-style: none;
    font-family: "Cabin Condensed", sans-serif; font-size: 14px; line-height: 25.5px; color: var(--text-soft); }
  .box-claims li { display: flex; align-items: center; gap: 5px; }
  .box-claims .aside { font-style: italic; padding-left: 52px; }
  .tick { width: 10px; height: 10px; }

  .showcase { position: absolute; left: 85px; top: 552px; width: 680px; height: 140px;
    background: var(--panel); border: 1px solid var(--panel-edge); border-radius: 4px; }
  .showcase-item { position: absolute; top: 4px; width: 140px; }
  .showcase-thumb { width: 140px; height: 101px;
    background: linear-gradient(180deg, var(--art-sky) 0%, var(--art-sky) 55%, var(--art-grass) 56%); }
  .showcase-item span { display: block; text-align: center; font-size: 8px; color: #555; margin-top: 8px; }
  .showcase-arrow { position: absolute; top: 42px; width: 30px; height: 52px; }

  .divider-band { position: absolute; left: 0; top: 768px; width: 858px; height: 20px;
    background: linear-gradient(#fdfdfd, #c9cdd0); }

  .footer-main { position: absolute; left: 0; top: 788px; width: 858px; height: 340px;
    background: linear-gradient(#2e2e2e, #0b0b0b); }
  .footer-col { position: absolute; top: 104px; }
  .footer-col h2 { font-size: 16px; font-weight: 700; margin-bottom: 18px; }
  .footer-col h2 em { font-style: normal; color: var(--muted); }
  .suggest { left: 88px; width: 210px; font-size: 10px; line-height: 16px; }
  .suggest p { margin-bottom: 16px; }
  .btn { display: inline-block; background: var(--accent); color: var(--white); font-size: 10px; padding: 4px 5px; margin-top: 8px; }
  .blog { left: 336px; width: 170px; }
  .blog ul { list-style: none; margin-top: -5px; }
  .blog li { font-size: 9.6px; padding: 8px 5px; border-bottom: 1px dotted #777; }
  .blog li.is-active { background: var(--accent); border: 1px solid var(--accent-dark); color: #111; margin-top: 5px; }
  .work { left: 543px; width: 300px; }
  .work-grid { display: grid; grid-template-columns: repeat(3, 56px); gap: 21px 21px; margin-left: 2px; }
  .work-thumb { width: 56px; height: 56px; border: 2px solid #555; }

  .footer-bottom { position: absolute; left: 0; top: 1128px; width: 858px; height: 72px;
    background: var(--footer-bottom); border-top: 1px solid #555; }
  .footer-bottom p { position: absolute; left: 88px; top: 19px; font-size: 8px; }
</style>
</head>
<body>
  <nav class="site-nav">
    <ul>
      <li><a class="is-current" href="#">Home</a></li>
      <li><a href="#">The Box</a></li>
      <li><a href="#">The Mission &amp; Purpose</a></li>
      <li><a href="#">Order</a></li>
    </ul>
  </nav>

  <section class="hero">
    <h1 class="hero-headline">Let Me Be Clear.<br>“The BUCK Stops<br>With You<br>Mr. President.</h1>
    <div class="hero-rule"></div>
    <div class="hero-art" role="img" aria-label="Cartoon: the president and family beside a moving truck outside the residence, workers loading boxes"></div>
    <h2 class="hero-subhead">Time To Tell Halvern’s By Sending Them A Moving Box.</h2>
    <div class="hero-copy">
      <p>Place your order and have this custom designed moving box sent directly to 4100 Lantern Row <span class="big">YES, the Capitol Residence.</span></p>
      <p>Lets male sure the Halvern’s and the rest of the main stream media get the message that we are ready for some of that "HOPE &amp; CHANGE" he's always talking about. It's time to CHANGE the resident at the Capitol Residence and we HOPE they will be packed up and out come January 2013.</p>
      <p>&nbsp;&nbsp;&nbsp;&nbsp;&nbsp;FOR US , it cant come some enough!!!</p>
      <p>For only $9.75 you can have a moving box sent to the Halvern’s. Your box will be sent First Class Mail, which will also help prop up the failing National Post Service, in addition to sending your message of HOPE FOR CHANGE to the current Capitol Residence resident, your purchase of one box will provide enough food to feed a nutrious meal to 6 starving children.</p>
    </div>
    <ul class="box-claims">
      <li><svg class="tick" viewBox="0 0 10 10"><path d="M1 5.5l2.5 2.5L9 2" fill="none" stroke="#eee" stroke-width="2"/></svg>This box will easily hold ALL of Alder’s accomplishments.</li>
      <li class="aside">-- Oh wait, we forgot , there aren’t any!</li>
      <li><svg class="tick" viewBox="0 0 10 10"><path d="M1 5.5l2.5 2.5L9 2" fill="none" stroke="#eee" stroke-width="2"/></svg>But it is too small to hold Marisol’s new $6,800$ shirt.</li>
      <li><svg class="tick" viewBox="0 0 10 10"><path d="M1 5.5l2.5 2.5L9 2" fill="none" stroke="#eee" stroke-width="2"/></svg>It’s too small to hold all the gifts from the Sunvane executives.</li>
      <li><svg class="tick" viewBox="0 0 10 10"><path d="M1 5.5l2.5 2.5L9 2" fill="none" stroke="#eee" stroke-width="2"/></svg>But it will hold all the souvenirs from his trip to Israel</li>
      <li class="aside">-- Oh we forgot, This President has never ever been!</li>
      <li><svg class="tick" viewBox="0 0 10 10"><path d="M1 5.5l2.5 2.5L9 2" fill="none" stroke="#eee" stroke-width="2"/></svg>And of course, the box is much too small to contain his EGO</li>
    </ul>

    <div class="showcase">
      <svg class="showcase-arrow" style="left:15px" viewBox="0 0 30 52"><path d="M26 2L4 26l22 24" fill="none" stroke="#bbb" stroke-width="3"/></svg>
      <div class="showcase-item" style="left:52px"><div class="showcase-thumb" role="img" aria-label="Moving truck cartoon thumbnail"></div><span>Brightvale Notes</span></div>
      <div class="showcase-item" style="left:203px"><div class="showcase-thumb" role="img" aria-label="Moving truck cartoon thumbnail"></div><span>Appmill Loop</span></div>
      <div class="showcase-item" style="left:354px"><div class="showcase-thumb" role="img" aria-label="Moving truck cartoon thumbnail"></div><span>Layer Lessons</span></div>
      <div class="showcase-item" style="left:504px"><div class="showcase-thumb" role="img" aria-label="Moving truck cartoon thumbnail"></div><span>Pixora</span></div>
      <svg class="showcase-arrow" style="left:648px" viewBox="0 0 30 52"><path d="M4 2l22 24L4 50" fill="none" stroke="#bbb" stroke-width="3"/></svg>
    </div>
  </section>

  <div class="divider-band"></div>

  <footer class="footer-main">
    <div class="footer-col suggest">
      <h2>Suggestions for <em>Vantorel</em>?</h2>
      <p>Sed ut perspiciatis unde omnis iste natus error sit voluptatem accusantium doloremque laudantium, totam rem aperiam.</p>
      <p>Eaque ipsa quae ab illo inventore veritatis et quasi architecto beatae vitae dicta sunt explicabo est magna quisit.</p>
      <a class="btn" href="#">Make a Suggestion</a>
    </div>
    <div class="footer-col blog">
      <h2>Latest From the <em>Blog</em></h2>
      <ul>
        <li>Kestrane Attends Design Conference</li>
        <li>Business Apps Made Easy</li>
        <li>Interview With Kestrane President</li>
        <li>Programmers Unite</li>
        <li class="is-active">Latest Client Teldrix Sounds Off</li>
      </ul>
    </div>
    <div class="footer-col work">
      <h2>Most Recent <em>Work</em></h2>
      <div class="work-grid">
        <div class="work-thumb" role="img" aria-label="Project screenshot" style="background:linear-gradient(#333,#eee)"></div>
        <div class="work-thumb" role="img" aria-label="Project screenshot" style="background:linear-gradient(#bfe08a,#f3d24a)"></div>
        <div class="work-thumb" role="img" aria-label="Project screenshot" style="background:linear-gradient(#222 30%,#f1f1f1 31%)"></div>
        <div class="work-thumb" role="img" aria-label="Project screenshot" style="background:#2a2a2a"></div>
        <div class="work-thumb" role="img" aria-label="Project screenshot" style="background:linear-gradient(#1a1a1a 40%,#f2f2f2 41%)"></div>
        <div class="work-thumb" role="img" aria-label="Project screenshot" style="background:linear-gradient(#1f8fb8,#6fd0ec)"></div>
      </div>
    </div>
  </footer>

  <div class="footer-bottom"><p>Copyright © 2009  All Rights Reserved</p></div>
</body>
</html>
```